Security company needs a business card design

We have a logo & we provide security services specialising in the construction site industry & remote areas. We are looking for a modern design preferably hi-tech as we provide hi-end specialised security services. We do not do pubs, clubs etc. Many of our employees are ex defence force & are highly qualified in covert ops etc.

Below are details that we would like on the front of the business card (I have attached our logo)
Logo + ML 738204519 (ML is abbreviation for "Master License")
We are also members of "GRONT" not sure if we need to put their logo on the business card or just make a reference to our membership (please advise - I have also attached their logo)

Company name: Vantor Ridge Security Services Pty Ltd

1) Employee name: Darren Okafor
Designation: Security Advisor / Director
Contact: M: 0451 307 984
e:darren@vantorridgesecurity-example.com.au (500cards 1st order)
2) Employee name: Gregory Okafor
Designation: Manager
Contact: M: 0437 215 640
e:gregory@vantorridgesecurity-example.com.au (250cards 1st order)
3) a generic card with no employee name or designation (250cards 1st order)

Company Address: 612 Wattlebend Rd, Coffs Harbour NSW 2450
T: +61 2 6621 4093 F: +61 2 6621 4058
E:admin@vantorridgesecurity-example.com.au
www.vantorridgesecurity-example.com.au

Below are details we provide which have been placed previously on the back of our business card:
Static Guards; Mobile Vehicle patrols; Alarm monitoring; 3 G CCTV Monitoring; Specialists in providing security requirements for construction sites & remote areas.
Updates

                                        Refer new pdf just uploaded

Target Market(s)

Security required for construction sites & remote areas

Industry/Entity Type

Construction

```html
<!DOCTYPE html>
<html lang="en">
<head>
<meta charset="utf-8">
<title>Vantor Ridge Security Services – Business Card</title>
<link rel="stylesheet" href="https://fonts.googleapis.com/css2?family=Questrial&family=Bitter:wght@800&display=swap">
<style>
  :root {
    --navy: #2b3593;
    --red: #e3202a;
    --badge-green: #3d7a2a;
    --badge-ring: #e8c63a;
    --paper: #ffffff;
    --ink: #3a3f6e;
    --stage: #e4e4e4;
    --ghost: rgba(43, 53, 147, 0.08);
  }
  * { margin: 0; padding: 0; box-sizing: border-box; }
  html, body {
    width: 1200px; height: 1200px; overflow: hidden;
    background: var(--stage);
  }
  .sheet { position: relative; width: 1200px; height: 1200px; }
  .card {
    position: absolute; left: 150px; width: 900px; height: 514px;
    background: var(--paper); overflow: hidden;
    box-shadow: 0 6px 18px rgba(0,0,0,0.18);
    font-family: "Questrial", "Century Gothic", sans-serif;
    color: var(--ink);
  }
  .card--front { top: 48px; }
  .card--back { top: 630px; }
  .card__art { position: absolute; inset: 0; width: 100%; height: 100%; }

  /* Front */
  .person { position: absolute; left: 70px; top: 58px; }
  .person__name {
    font-size: 46px; color: var(--navy); font-weight: 400; letter-spacing: 0.5px;
  }
  .person__role { font-size: 16px; margin: 4px 0 0 150px; color: var(--ink); }
  .contact {
    position: absolute; left: 110px; top: 148px; list-style: none;
    font-size: 16px; line-height: 25px; color: var(--ink);
  }
  .contact__gap { height: 14px; }
  .membership-badge {
    position: absolute; left: 40px; top: 262px; width: 42px; height: 42px;
    border-radius: 50%; background: var(--badge-green);
    border: 3px solid var(--badge-ring);
  }
  .brand {
    position: absolute; left: 560px; top: 130px; width: 300px;
    display: flex; align-items: center; gap: 14px;
  }
  .brand__mark { width: 26px; height: 26px; background: var(--navy); flex: none; }
  .brand__name {
    font-size: 36px; color: var(--navy); letter-spacing: 1px; line-height: 1.1;
  }
  .licence {
    position: absolute; left: 600px; top: 262px; font-size: 17px; color: var(--ink);
  }

  /* Back */
  .company-title {
    position: absolute; top: 34px; left: 0; width: 100%; text-align: center;
    font-family: "Bitter", "Bookman Old Style", serif; font-weight: 800;
    font-size: 44px; color: var(--navy); letter-spacing: 0.5px;
  }
  .ghost-brand {
    position: absolute; top: 130px; left: 0; width: 100%; text-align: center;
    font-size: 92px; color: var(--ghost); letter-spacing: 4px;
  }
  .services {
    position: absolute; list-style: disc; font-size: 19px; line-height: 25px;
    color: var(--navy);
  }
  .services--primary { left: 160px; top: 116px; }
  .services--secondary { left: 510px; top: 166px; }
  .specialty {
    position: absolute; top: 304px; left: 0; width: 100%; text-align: center;
    font-family: "Bitter", "Bookman Old Style", serif; font-weight: 800;
    color: var(--navy);
  }
  .specialty__lead { font-size: 26px; }
  .specialty__focus { font-size: 29px; margin-top: 2px; }
</style>
</head>
<body>
<main class="sheet">

  <section class="card card--front" aria-label="Business card front">
    <svg class="card__art" viewBox="0 0 900 514" aria-hidden="true">
      <path d="M540 514 Q 780 480 900 320 L900 514 Z" fill="var(--red)"/>
      <path d="M0 330 Q 90 470 560 508" fill="none" stroke="var(--red)" stroke-width="6"/>
      <path d="M0 350 Q 110 486 520 512" fill="none" stroke="var(--navy)" stroke-width="5"/>
    </svg>

    <div class="person">
      <h1 class="person__name">Darren Okafor</h1>
      <p class="person__role">security advisor / director</p>
    </div>

    <ul class="contact">
      <li>Mobile: (+61) 0451 307 984</li>
      <li>Email: darren@vantorridgesecurity-example.com.au</li>
      <li class="contact__gap"></li>
      <li>612 Wattlebend Rd, Tarrengo Bay NSW 2999</li>
      <li>Telephone: +61 2 6621 4093</li>
      <li>Fax: +61 2 6621 4058</li>
      <li>Email: admin@vantorridgesecurity-example.com.au</li>
    </ul>

    <div class="membership-badge" aria-label="GRONT membership badge"></div>

    <div class="brand">
      <span class="brand__mark"></span>
      <span class="brand__name">VANTOR RIDGE</span>
    </div>
    <p class="licence">ML 738204519</p>
  </section>

  <section class="card card--back" aria-label="Business card back">
    <svg class="card__art" viewBox="0 0 900 514" aria-hidden="true">
      <path d="M330 514 Q 700 480 900 330 L900 514 Z" fill="var(--navy)"/>
      <path d="M0 220 Q 60 440 460 502" fill="none" stroke="var(--navy)" stroke-width="5"/>
      <path d="M0 240 Q 80 450 420 510" fill="none" stroke="var(--red)" stroke-width="6"/>
    </svg>

    <h2 class="company-title">VANTOR RIDGE SECURITY SERVICES</h2>
    <div class="ghost-brand" aria-hidden="true">VANTOR RIDGE</div>

    <ul class="services services--primary">
      <li>Alarm Monitoring / Response</li>
      <li>Mobile Vehicle Patrols</li>
      <li>Asset Protection (GPS Tracking)</li>
      <li>Tactical Operations</li>
      <li>Security Briefs &amp; Incident Reporting</li>
    </ul>
    <ul class="services services--secondary">
      <li>Live 3G IP/IR Systems</li>
      <li>Hunting Cams</li>
      <li>Foot Patrols</li>
      <li>Static Guards</li>
      <li>Call Outs</li>
    </ul>

    <div class="specialty">
      <p class="specialty__lead">We specialise in</p>
      <p class="specialty__focus">CONSTRUCTION SITES &amp; REMOTE AREAS</p>
    </div>
  </section>

</main>
</body>
</html>
```